Velmor Haulage Heavy Goods Transport web design

I have a client who requires a new web site design.
They are Velmor Haulage in the UK.
They have a current site which needs updating with a fresh look and feel using modern design ideas.
Their current site is velmorhaulage.co.uk
I will use your design to build a new CMS site for them using Django.
I only require the layered PSD files, main page design plus a sub page showing navigation changes and layout changes between pages.
The site needs to have the same sections as the current site plus:
1) Proof of delivery downloads system (customer logs in to access their delivery documents).
2) CMS system will allow them to add pages so the menu system needs to be designed such that it can expand.
3) A contact page with a contact form and a Google map will be used.
4) No flash.
5) Slideshow banners (using JQuery will be used).
I like the following type of designs:
www.billotrix.com/pricing.html
www.ledgerpine.com/
quorvel.ly/features
tabnestix.com/
I am looking for a designer to work with me designing other web design projects as well so this project will be used as a test bed for us working together.
The budget for our client designs is between £120 and £200 depending on functionality requirements. This site has a budget of £150.
Please submit your quotes by email to dharlow@brenquay.com
Industrial business customers
Build

```html
<!DOCTYPE html>
<html lang="en">
<head>
<meta charset="utf-8">
<title>Velmor Haulage – Heavy Goods Transport</title>
<link rel="stylesheet" href="https://fonts.googleapis.com/css2?family=Nunito+Sans:wght@400;600;700&display=swap">
<style>
  :root {
    --page-bg: #232323;
    --band-bg: #2c2c2c;
    --header-dark: #0e2418;
    --header-mid: #1d3c2b;
    --nav-bg: #1a1a1a;
    --orange: #f7931e;
    --orange-soft: #f5a54a;
    --text: #d2d2d2;
    --text-dim: #9a9a9a;
    --white: #ffffff;
    --rule: #444444;
    --green-btn: #3a6b10;
  }
  * { box-sizing: border-box; margin: 0; padding: 0; }
  html, body { width: 1157px; height: 1200px; overflow: hidden; background: var(--page-bg); }
  body { font-family: "Nunito Sans", Arial, sans-serif; color: var(--text); }
  a { color: inherit; text-decoration: none; }

  .stage { position: relative; width: 1000px; height: 1037px; transform: scale(1.157); transform-origin: 0 0; background: var(--page-bg); }
  .abs { position: absolute; }

  /* header */
  .top-strip { left: 0; top: 0; width: 1000px; height: 10px; background: repeating-linear-gradient(135deg, #2a2a2a 0 3px, #1e1e1e 3px 6px); }
  .header { left: 0; top: 10px; width: 1000px; height: 103px; background: linear-gradient(180deg, var(--header-mid), var(--header-dark)); }
  .brand { left: 25px; top: 44px; display: flex; align-items: center; gap: 10px; color: var(--orange-soft); font-size: 30px; font-weight: 700; letter-spacing: .5px; }
  .brand-mark { width: 22px; height: 22px; background: var(--orange-soft); }
  .account-links { right: 28px; top: 17px; font-size: 13px; color: #b9b9b9; }
  .account-links span { margin: 0 5px; color: #777; }

  /* band behind slider */
  .band { left: 0; top: 113px; width: 1000px; height: 362px; background: var(--band-bg); }
  .band-accent { top: 113px; width: 20px; height: 15px; background: var(--orange); }

  /* navigation */
  .main-nav { left: 20px; top: 113px; width: 960px; height: 42px; background: var(--nav-bg); display: flex; padding-left: 27px; font-size: 13px; color: #e6e6e6; }
  .main-nav a { display: flex; align-items: center; justify-content: center; height: 42px; }
  .main-nav .is-active { color: var(--orange); background: linear-gradient(180deg, #3a3a3a, #262626); border-bottom: 3px solid var(--orange); }

  /* slider */
  .hero { left: 20px; top: 155px; width: 960px; height: 345px; background: linear-gradient(100deg, #7d7350 0%, #8f8b7b 30%, #6f7072 55%, #5a5c5e 100%); border-bottom: 3px solid #e9e9e9; }
  .hero-pager { left: 838px; top: 481px; width: 96px; height: 19px; background: #e4e4e4; border-radius: 3px 3px 0 0; display: flex; gap: 5px; align-items: center; justify-content: center; }
  .hero-pager i { width: 8px; height: 8px; border-radius: 50%; background: #2a2a2a; }
  .hero-pager i.on { background: #2d6b2a; }

  /* content */
  .section-title { font-size: 18px; font-weight: 600; color: var(--white); }
  .rule { height: 1px; background: var(--rule); }
  .thumb { left: 20px; top: 576px; width: 189px; height: 134px; border: 1px solid #555; padding: 4px; }
  .thumb div { width: 100%; height: 100%; background: linear-gradient(160deg, #d9dde0 0%, #4d5a4c 50%, #7a7040 100%); }
  .intro-lead { left: 225px; top: 578px; width: 480px; font-size: 14px; line-height: 18px; color: #e2e2e2; }
  .intro-body { left: 225px; top: 623px; width: 480px; font-size: 12.3px; line-height: 18px; color: var(--text-dim); }
  .more-link { left: 227px; top: 703px; display: flex; align-items: center; gap: 6px; font-size: 13px; color: var(--orange); text-decoration: underline; }

  .services { left: 30px; top: 801px; display: flex; }
  .services ul { list-style: none; }
  .services li { display: flex; align-items: center; gap: 8px; height: 25px; font-size: 12.3px; color: #bdbdbd; }

  /* sidebar */
  .search-box { left: 758px; top: 523px; width: 222px; height: 107px; border-radius: 4px; background: linear-gradient(180deg, #4a4a4a, #333 60%, #3a3a3a); padding: 14px 17px; }
  .search-box h3 { font-size: 15px; font-weight: 600; color: var(--white); margin-bottom: 10px; }
  .search-field { display: flex; }
  .search-field span { width: 152px; height: 26px; background: #fff; }
  .search-field b { width: 34px; height: 26px; background: var(--green-btn); color: #fff; font-size: 12px; font-weight: 600; display: flex; align-items: center; justify-content: center; }
  .testi-head { left: 758px; top: 640px; width: 219px; height: 27px; background: #1a1a1a; padding: 4px 7px; font-size: 15px; color: var(--white); display: flex; justify-content: space-between; }
  .testi-head small { color: #777; font-size: 13px; }
  .testi-photo { left: 764px; top: 674px; width: 96px; height: 63px; border: 1px solid #bbb; padding: 3px; background: #eee; }
  .testi-photo div { width: 100%; height: 100%; background: linear-gradient(180deg, #e9e9e9, #9c9c9c); }
  .testi-meta { left: 869px; top: 700px; font-size: 12.5px; line-height: 19px; color: #dcdcdc; }
  .testi-quote { left: 763px; top: 748px; width: 220px; font-size: 12.3px; line-height: 18px; color: #bdbdbd; }
  .delivery { left: 758px; top: 812px; width: 222px; height: 113px; border-radius: 4px; background: linear-gradient(160deg, #4b4b4b, #2f2f2f 70%); overflow: hidden; }
  .delivery .kicker { position: absolute; left: 17px; top: 18px; font-size: 22px; color: #cfcfcf; }
  .delivery .big { position: absolute; left: 8px; top: 36px; font-size: 40px; color: var(--white); letter-spacing: 1px; }
  .delivery .go { position: absolute; left: 101px; top: 83px; font-size: 12px; color: #999; text-decoration: underline; }
  .delivery .truck { position: absolute; left: 160px; top: 70px; width: 62px; height: 43px; background: linear-gradient(90deg, var(--orange), #ededed 40%); border-radius: 3px; }

  /* footer */
  .footer-rule { left: 13px; top: 949px; width: 974px; height: 1px; background: var(--orange); }
  .footer-links { left: 36px; top: 975px; font-size: 11.5px; color: #a9a9a9; }
  .footer-links span { margin: 0 5px; color: #666; }
  .copyright { left: 34px; top: 997px; font-size: 12.3px; color: #7d7d7d; }
  .contact { left: 856px; top: 966px; font-size: 11.5px; line-height: 17px; color: #8a8a8a; }
  .contact b { color: #cfcfcf; font-weight: 600; }
  .social { left: 857px; top: 1002px; display: flex; gap: 6px; }
  .social i { width: 18px; height: 17px; background: #6d6d6d; }
</style>
</head>
<body>
<div class="stage">
  <div class="abs top-strip"></div>
  <header class="abs header"></header>
  <div class="abs brand"><span class="brand-mark"></span>Velmor Haulage</div>
  <div class="abs account-links">Welcome Guest<span>|</span>Join us<span>|</span>Log in</div>

  <div class="abs band"></div>
  <div class="abs band-accent" style="left:0"></div>
  <div class="abs band-accent" style="left:980px"></div>

  <nav class="abs main-nav">
    <a class="is-active" style="width:106px">Home</a>
    <a style="width:100px">About Us</a>
    <a style="width:112px">Culture</a>
    <a style="width:100px">Our Team</a>
    <a style="width:115px">Depots</a>
    <a style="width:115px">Contact Us</a>
    <a style="width:130px">Notice Board</a>
    <a style="width:127px">Testimonials</a>
  </nav>

  <div class="abs hero" role="img" aria-label="Photo of a company lorry driving along a motorway beside a grass verge"></div>
  <div class="abs hero-pager"><i></i><i class="on"></i><i></i><i></i><i></i></div>

  <h2 class="abs section-title" style="left:21px;top:527px">Welcome to Our Website</h2>
  <div class="abs rule" style="left:20px;top:558px;width:692px"></div>
  <div class="abs thumb"><div role="img" aria-label="Photo of a company lorry parked on grass"></div></div>
  <p class="abs intro-lead">Ut enim ad minima veniam, quis nostrum exercitationem ullam corporis suscipit laboriosam</p>
  <p class="abs intro-body">Sed ut perspiciatis unde omnis iste natus error sit voluptatem accusantium doloremque laudantium, totam rem aperiam, eaque ipsa quae ab illo inventore veritatis et quasi architecto beatae vitae dicta sunt explicabo. Nemo enim ipsam voluptatem quia voluptas sit aspernatur aut odit aut fugit, sed quia consequuntur</p>
  <a class="abs more-link">
    <svg width="13" height="13" viewBox="0 0 13 13"><circle cx="6.5" cy="6.5" r="6.5" fill="#f7931e"/><path d="M5 3.5 8 6.5 5 9.5" stroke="#232323" stroke-width="1.8" fill="none"/></svg>
    More About us
  </a>

  <h2 class="abs section-title" style="left:21px;top:747px">Main Services</h2>
  <div class="abs rule" style="left:20px;top:779px;width:692px"></div>
  <div class="abs services">
    <ul style="width:170px">
      <li><svg width="12" height="10" viewBox="0 0 12 10"><path d="M1 5 4.5 8.5 11 1" stroke="#f7a431" stroke-width="2" fill="none"/></svg>Mauris nec felis enim</li>
      <li><svg width="12" height="10" viewBox="0 0 12 10"><path d="M1 5 4.5 8.5 11 1" stroke="#f7a431" stroke-width="2" fill="none"/></svg>Maecenas in sapien</li>
      <li><svg width="12" height="10" viewBox="0 0 12 10"><path d="M1 5 4.5 8.5 11 1" stroke="#f7a431" stroke-width="2" fill="none"/></svg>Donec vel torto</li>
      <li><svg width="12" height="10" viewBox="0 0 12 10"><path d="M1 5 4.5 8.5 11 1" stroke="#f7a431" stroke-width="2" fill="none"/></svg>Donec in mi nec magna</li>
      <li><svg width="12" height="10" viewBox="0 0 12 10"><path d="M1 5 4.5 8.5 11 1" stroke="#f7a431" stroke-width="2" fill="none"/></svg>Sed vel nulla vel</li>
    </ul>
    <ul style="width:170px">
      <li><svg width="12" height="10" viewBox="0 0 12 10"><path d="M1 5 4.5 8.5 11 1" stroke="#f7a431" stroke-width="2" fill="none"/></svg>Mauris nec felis enim</li>
      <li><svg width="12" height="10" viewBox="0 0 12 10"><path d="M1 5 4.5 8.5 11 1" stroke="#f7a431" stroke-width="2" fill="none"/></svg>Maecenas in sapien</li>
      <li><svg width="12" height="10" viewBox="0 0 12 10"><path d="M1 5 4.5 8.5 11 1" stroke="#f7a431" stroke-width="2" fill="none"/></svg>Donec vel torto</li>
      <li><svg width="12" height="10" viewBox="0 0 12 10"><path d="M1 5 4.5 8.5 11 1" stroke="#f7a431" stroke-width="2" fill="none"/></svg>Donec in mi nec magna</li>
      <li><svg width="12" height="10" viewBox="0 0 12 10"><path d="M1 5 4.5 8.5 11 1" stroke="#f7a431" stroke-width="2" fill="none"/></svg>Sed vel nulla vel</li>
    </ul>
    <ul style="width:177px">
      <li><svg width="12" height="10" viewBox="0 0 12 10"><path d="M1 5 4.5 8.5 11 1" stroke="#f7a431" stroke-width="2" fill="none"/></svg>Mauris nec felis enim</li>
      <li><svg width="12" height="10" viewBox="0 0 12 10"><path d="M1 5 4.5 8.5 11 1" stroke="#f7a431" stroke-width="2" fill="none"/></svg>Maecenas in sapien</li>
      <li><svg width="12" height="10" viewBox="0 0 12 10"><path d="M1 5 4.5 8.5 11 1" stroke="#f7a431" stroke-width="2" fill="none"/></svg>Donec vel torto</li>
      <li><svg width="12" height="10" viewBox="0 0 12 10"><path d="M1 5 4.5 8.5 11 1" stroke="#f7a431" stroke-width="2" fill="none"/></svg>Donec in mi nec magna</li>
      <li><svg width="12" height="10" viewBox="0 0 12 10"><path d="M1 5 4.5 8.5 11 1" stroke="#f7a431" stroke-width="2" fill="none"/></svg>Sed vel nulla vel</li>
    </ul>
    <ul style="width:170px">
      <li><svg width="12" height="10" viewBox="0 0 12 10"><path d="M1 5 4.5 8.5 11 1" stroke="#f7a431" stroke-width="2" fill="none"/></svg>Mauris nec felis enim</li>
      <li><svg width="12" height="10" viewBox="0 0 12 10"><path d="M1 5 4.5 8.5 11 1" stroke="#f7a431" stroke-width="2" fill="none"/></svg>Maecenas in sapien</li>
      <li><svg width="12" height="10" viewBox="0 0 12 10"><path d="M1 5 4.5 8.5 11 1" stroke="#f7a431" stroke-width="2" fill="none"/></svg>Donec vel torto</li>
    </ul>
  </div>

  <aside>
    <div class="abs search-box">
      <h3>Search</h3>
      <div class="search-field"><span></span><b>Go!</b></div>
    </div>
    <div class="abs testi-head">Testimonials <small>&#10216;&#10217;</small></div>
    <div class="abs testi-photo"><div role="img" aria-label="Portrait photo of the customer giving the testimonial"></div></div>
    <div class="abs testi-meta">Owen<br>feb 03,2012</div>
    <p class="abs testi-quote">There is no one who loves pain itself, who seeks after it and wants to have it, simply because it is pain</p>
    <div class="abs delivery">
      <span class="kicker">Trucking</span>
      <span class="big">DELIVERY</span>
      <span class="go">Click here</span>
      <span class="truck" role="img" aria-label="Illustration of a small delivery truck"></span>
    </div>
  </aside>

  <footer>
    <div class="abs footer-rule"></div>
    <div class="abs footer-links">Home<span>|</span>About Us<span>|</span>Culture<span>|</span>Our Team<span>|</span>Depots<span>|</span>Contact Us<span>|</span>Notice Board<span>|</span>Testimonials</div>
    <div class="abs copyright">© All 2012 copyrights.velmorhaulage.received</div>
    <div class="abs contact">Phone : <b>01632 960418,</b><br>E-Mail : <b>01632 960527</b></div>
    <div class="abs social"><i></i><i></i><i></i><i></i><i></i></div>
  </footer>
</div>
</body>
</html>
```